Real Estate Business Cards

Looking for a clean, sharp and professional look for our Real Estate investment Fund that invests in Multi Family Apartment buildings.

Target Market(s)

Real Estate Fund

Industry/Entity Type

Real Estate

Contact Information for Business Card

Company Description: Real Estate Investment Fund
Company Name: KRV Holdings
Name: Marcus Tovell
Cell: (917) 482-0957
Email: marcus@krvholdings-example.com
Website: www.krvholdings-example.com
Address: 148, 7th Street, Brooklyn NY 11217

Colors

Designer to choose colors to be used in the design.

Requirements
Nice to have
• Colors to match logo

```html
<!DOCTYPE html>
<html lang="en">
<head>
<meta charset="utf-8">
<title>KRV Holdings – Business Card</title>
<link rel="stylesheet" href="https://fonts.googleapis.com/css2?family=Cinzel:wght@400&family=Montserrat:wght@300;400&display=swap">
<style>
  :root {
    --brand-blue: #1f6fa8;
    --ink-grey: #4a4a4a;
    --card-white: #ffffff;
  }
  * { margin: 0; padding: 0; box-sizing: border-box; }
  html, body {
    width: 1200px;
    height: 720px;
    overflow: hidden;
    background: var(--card-white);
  }
  .card {
    position: relative;
    width: 1200px;
    height: 720px;
    background: var(--card-white);
    color: var(--ink-grey);
    font-family: "Montserrat", Arial, sans-serif;
    font-weight: 300;
  }
  .brand {
    position: absolute;
    left: 34px;
    top: 250px;
    width: 560px;
    display: flex;
    flex-direction: column;
    align-items: center;
  }
  .brand-mark {
    width: 110px;
    height: 110px;
    background: var(--brand-blue);
    margin-bottom: 68px;
  }
  .brand-name {
    font-family: "Cinzel", Georgia, serif;
    font-weight: 400;
    font-size: 54px;
    line-height: 1;
    color: var(--brand-blue);
    white-space: nowrap;
  }
  .divider {
    position: absolute;
    left: 595px;
    top: 217px;
    width: 2px;
    height: 490px;
    background: var(--brand-blue);
  }
  .contact {
    position: absolute;
    left: 662px;
    top: 212px;
  }
  .person-name {
    font-family: "Cinzel", Georgia, serif;
    font-weight: 400;
    font-size: 38px;
    line-height: 42px;
    letter-spacing: 1px;
    color: var(--brand-blue);
  }
  .person-title {
    font-size: 29px;
    line-height: 34px;
    margin-top: -2px;
  }
  .address {
    font-size: 29px;
    line-height: 33px;
    margin-top: 10px;
    font-style: normal;
  }
  .channels {
    list-style: none;
    margin-top: 14px;
  }
  .channel {
    display: flex;
    align-items: center;
    height: 37px;
    font-size: 25px;
  }
  .channel-icon {
    width: 26px;
    height: 26px;
    margin-right: 19px;
    flex: none;
  }
</style>
</head>
<body>
  <div class="card">
    <div class="brand">
      <div class="brand-mark"></div>
      <div class="brand-name">KRV HOLDINGS</div>
    </div>

    <div class="divider"></div>

    <div class="contact">
      <h1 class="person-name">MARCUS TOVELL</h1>
      <p class="person-title">Fund Manager</p>
      <address class="address">148, 7th Street<br>Brooklyn NY 11217</address>
      <ul class="channels">
        <li class="channel">
          <svg class="channel-icon" viewBox="0 0 24 24" aria-hidden="true">
            <path fill="var(--brand-blue)" d="M6.6 10.8a15.1 15.1 0 0 0 6.6 6.6l2.2-2.2a1 1 0 0 1 1-.25 11.4 11.4 0 0 0 3.6.57 1 1 0 0 1 1 1V20a1 1 0 0 1-1 1A17 17 0 0 1 3 4a1 1 0 0 1 1-1h3.5a1 1 0 0 1 1 1c0 1.25.2 2.45.57 3.57a1 1 0 0 1-.25 1z"/>
          </svg>
          <span>(917) 482-0957</span>
        </li>
        <li class="channel">
          <svg class="channel-icon" viewBox="0 0 24 24" aria-hidden="true">
            <rect x="2" y="5" width="20" height="14" fill="none" stroke="var(--brand-blue)" stroke-width="2"/>
            <path d="M2.5 5.5 12 13l9.5-7.5" fill="none" stroke="var(--brand-blue)" stroke-width="2"/>
          </svg>
          <span>marcus@krvholdings-example.com</span>
        </li>
        <li class="channel">
          <svg class="channel-icon" viewBox="0 0 24 24" aria-hidden="true">
            <circle cx="12" cy="12" r="10" fill="var(--brand-blue)"/>
            <g fill="none" stroke="var(--card-white)" stroke-width="1.4">
              <ellipse cx="12" cy="12" rx="4" ry="10"/>
              <line x1="2" y1="12" x2="22" y2="12"/>
              <line x1="12" y1="2" x2="12" y2="22"/>
              <path d="M4 7h16M4 17h16"/>
            </g>
          </svg>
          <span>www.krvholdings-example.com</span>
        </li>
      </ul>
    </div>
  </div>
</body>
</html>
```